Simple elegant feminine design - Going out on my own as a Mortgage Broker.
My thoughts are the following details on the Front, middle of the card possibly? Phone and email smaller font than my name?
Marnie Veltrin
Finance Specialist
p: 0438 215 962
e: marnie@veltrinlending.com.au
Bottom of the card
residential / commercial / equipment
I would like the Font in Rose Gold maybe white or black background? or Possibly a stone grey - are you able to do a few options? I'd like them embossed
Then I had an idea as a simple logo as per the attached if you get the idea in my scribble, my initials, capital M attached to a small v that leads/follows into a circle? Thicker Font In Rose Gold, middle of the card at the back.
Very open to ideas though and what colour you think would look better with the Rose Gold.
Thanks so much for your help, I am not very creative and savvy with this stuff :-)
Industry/Entity Type
Finance
Contact Information for Business Card
Marnie Veltrin
p: 0438 215 962
Look and feel

```html
<!DOCTYPE html>
<html lang="en">
<head>
<meta charset="utf-8">
<title>Marnie Veltrin – Business Cards</title>
<link rel="stylesheet" href="https://fonts.googleapis.com/css2?family=Didact+Gothic&family=Montserrat:wght@500&display=swap">
<style>
  :root {
    --backdrop: #8b8d8c;
    --card-light: #f1f1f0;
    --card-dark: #2a2b2f;
    --rose-gold: #c9935c;
    --rose-gold-soft: #d8a46c;
    --wave-light: #fbf8f3;
    --wave-shade: #e9e4dc;
  }
  * { margin: 0; padding: 0; box-sizing: border-box; }
  html, body {
    width: 1200px;
    height: 1139px;
    overflow: hidden;
    background: var(--backdrop);
  }
  .sheet {
    position: relative;
    width: 1200px;
    height: 1139px;
  }
  .card {
    position: absolute;
    left: 274px;
    width: 660px;
    height: 366px;
  }
  .card--front {
    top: 151px;
    background: var(--card-light);
  }
  .card--back {
    top: 595px;
    background: var(--card-dark);
    color: var(--rose-gold);
    font-family: "Didact Gothic", sans-serif;
    text-align: center;
  }
  .wave-field {
    position: absolute;
    left: 0;
    top: 0;
    width: 660px;
    height: 265px;
    background: linear-gradient(180deg, var(--wave-light) 0%, var(--wave-shade) 50%, var(--wave-light) 100%);
  }
  .name-wide {
    font-family: "Montserrat", sans-serif;
    font-weight: 500;
    color: var(--rose-gold);
    letter-spacing: 0.55em;
    text-transform: uppercase;
    white-space: nowrap;
  }
  .card--front .name-wide {
    position: absolute;
    left: 0;
    right: 0;
    top: 294px;
    text-align: center;
    font-size: 28px;
    padding-left: 0.55em;
  }
  .brand-mark {
    position: absolute;
    left: 0;
    right: 0;
    top: 58px;
    display: flex;
    align-items: center;
    justify-content: center;
    gap: 10px;
    font-size: 17px;
    color: var(--rose-gold);
  }
  .brand-mark svg { display: block; }
  .card--back .name-wide {
    position: absolute;
    left: 0;
    right: 0;
    top: 126px;
    font-size: 22px;
    padding-left: 0.55em;
  }
  .role {
    position: absolute;
    left: 0; right: 0;
    top: 156px;
    font-size: 17px;
    color: var(--rose-gold-soft);
  }
  .divider {
    position: absolute;
    left: 303px;
    top: 205px;
    width: 53px;
    height: 1px;
    background: var(--rose-gold);
  }
  .contact {
    position: absolute;
    left: 0; right: 0;
    font-size: 17px;
    color: var(--rose-gold-soft);
  }
  .contact--phone { top: 232px; }
  .contact--email { top: 257px; }
  .services {
    position: absolute;
    left: 0; right: 0;
    top: 304px;
    font-size: 17px;
    color: var(--rose-gold);
  }
</style>
</head>
<body>
  <main class="sheet">
    <section class="card card--front" aria-label="Card front">
      <div class="wave-field" role="img" aria-label="Embossed pattern of fine rose gold wavy lines"></div>
      <h1 class="name-wide">Marnie Veltrin</h1>
    </section>

    <section class="card card--back" aria-label="Card back">
      <div class="brand-mark">
        <svg width="14" height="14" viewBox="0 0 14 14" aria-hidden="true">
          <circle cx="7" cy="7" r="6" fill="none" stroke="currentColor" stroke-width="1.5"/>
        </svg>
        <span>Veltrin Lending</span>
      </div>
      <h2 class="name-wide">Marnie Veltrin</h2>
      <p class="role">Finance Specialist</p>
      <div class="divider"></div>
      <p class="contact contact--phone">0438 215 962</p>
      <p class="contact contact--email">marnie@veltrinlending.com.au</p>
      <p class="services">Residential . Commercial . Equipment</p>
    </section>
  </main>
</body>
</html>
```